Medical Flyer Design for Diabetic Retinopathy

Our company (an eye care provider in Kansas City) is seeking a high quality medical flyer design that will integrate preexisting copy that has been written to be distributed to referring physicians. The design should position our company as a modern, leading provider of eye care services to our peers in the medical community. The final product can include a front and back design.

Target Market(s)

Medical Professionals

Industry/Entity Type

Medical

Font styles to use
Sans Serif

Colors
34b8a5
33a6d7
3377b5
f79021

Requirements
Should not have
• typos

```html
<!DOCTYPE html>
<html lang="en">
<head>
<meta charset="utf-8">
<title>Diabetic Retinopathy – Physician Flyer</title>
<link href="https://fonts.googleapis.com/css2?family=Roboto+Condensed:wght@400;700&family=Roboto:wght@400;500&display=swap" rel="stylesheet">
<style>
  :root{
    --teal:#34b8a5;
    --teal-deep:#249c8f;
    --sky:#33a6d7;
    --blue:#3377b5;
    --orange:#f79021;
    --ink:#2d2d2d;
    --heading-teal:#2aa89a;
    --white:#ffffff;
  }
  *{box-sizing:border-box;margin:0;padding:0}
  html,body{width:900px;height:1200px;overflow:hidden;background:#fff}
  .flyer{position:relative;width:900px;height:1200px;overflow:hidden;background:var(--white);font-family:"Roboto",Arial,sans-serif;color:var(--ink)}

  .hero-photo{position:absolute;left:0;top:0;width:900px;height:560px;
    background:linear-gradient(120deg,#e9dfd8 0%,#d9b59d 28%,#c99a7d 42%,#eef0f2 62%,#f6f7f8 100%)}

  .brand{position:absolute;right:28px;top:22px;display:flex;align-items:center;gap:14px;
    background:rgba(255,255,255,.92);padding:14px 20px}
  .brand-mark{width:44px;height:44px;background:var(--orange)}
  .brand-name{font-family:"Roboto Condensed",Arial,sans-serif;font-weight:700;font-size:38px;color:var(--heading-teal);line-height:1}

  .wave-top{position:absolute;left:0;top:400px;width:900px;height:170px}

  .disease-types{position:absolute;left:410px;top:240px;width:466px;height:268px;
    background:var(--orange);border-radius:26px 26px 0 0;padding:22px 22px 0 22px;color:var(--white);z-index:2}
  .disease-types h2{font-family:"Roboto Condensed",Arial,sans-serif;font-weight:700;font-size:27px;letter-spacing:.3px;margin-bottom:10px}
  .disease-types h3{font-family:"Roboto Condensed",Arial,sans-serif;font-weight:700;font-size:19px;color:#1f6fa8;margin-bottom:12px}
  .disease-types p{font-size:13.6px;line-height:1.32;margin-bottom:7px}

  .edge-strip{position:absolute;left:0;top:610px;width:18px;height:560px;background:var(--teal)}

  .intro{position:absolute;left:40px;top:556px;width:372px}
  .kicker{font-family:"Roboto Condensed",Arial,sans-serif;font-weight:700;font-size:24px;color:var(--heading-teal);line-height:1}
  .intro h1{font-family:"Roboto Condensed",Arial,sans-serif;font-weight:700;font-size:35px;color:var(--heading-teal);line-height:1.05;margin-bottom:10px;white-space:nowrap}
  .intro p{font-size:14px;line-height:1.3}
  .facts h2{font-family:"Roboto Condensed",Arial,sans-serif;font-weight:700;font-size:26px;color:var(--heading-teal);margin:22px 0 12px;white-space:nowrap}
  .facts ul{list-style:none}
  .facts li{position:relative;padding-left:14px;font-size:14px;line-height:1.3;margin-bottom:9px}
  .facts li::before{content:"";position:absolute;left:0;top:7px;width:5px;height:5px;border-radius:50%;background:var(--heading-teal)}

  .clinical{position:absolute;left:432px;top:556px;width:444px;height:620px;
    background:linear-gradient(180deg,var(--teal-deep),var(--teal));color:var(--white);padding:20px 22px 0 22px}
  .clinical h2{font-family:"Roboto Condensed",Arial,sans-serif;font-weight:700;font-size:22.5px;line-height:1.1;letter-spacing:.2px}
  .clinical h2 .accent{color:var(--orange)}
  .clinical ul{list-style:none}
  .clinical li{position:relative;padding-left:11px;font-size:13.8px;line-height:1.3}
  .clinical li::before{content:"";position:absolute;left:0;top:7px;width:4px;height:4px;border-radius:50%;background:var(--white)}
  .signs{margin:10px 0 14px}
  .signs li{margin-bottom:10px}
  .clinical p{font-size:14px;line-height:1.32;margin:10px 0 16px}
  .strategies{display:flex;gap:14px;margin-top:12px}
  .strategies ul:first-child{width:220px}
  .strategies li{margin-bottom:10px}

  .wave-bottom{position:absolute;left:0;top:1090px;width:900px;height:110px;z-index:3}
</style>
</head>
<body>
<main class="flyer">
  <div class="hero-photo" role="img" aria-label="Photo of an eye doctor applying drops to a patient's eye"></div>

  <div class="brand">
    <span class="brand-mark"></span>
    <span class="brand-name">Brightfield Eye Care</span>
  </div>

  <svg class="wave-top" viewBox="0 0 900 170" preserveAspectRatio="none" aria-hidden="true">
    <path d="M0,118 Q430,150 900,30 L900,170 L0,170 Z" fill="#ffffff"/>
    <path d="M0,62 Q430,112 900,0 L900,30 Q430,150 0,118 Z" fill="var(--blue)"/>
  </svg>

  <section class="disease-types">
    <h2>TYPES OF DIABETIC EYE DISEASE</h2>
    <h3>Non-proliferative diabetic retinopathy (NPDR)</h3>
    <p>NPDR is characterized by bleeding (dot-blot hemorrhages), microaneurysms, exudate, and edema. NPDR is graded as mild, moderate or severe and may be accompanied by clinically significant macular edema that requires treatment to prevent vision loss.</p>
    <p>Proliferative diabetic retinopathy (PDR). Of the diabetic eye diseases, PDR has the greatest risk of visual loss.</p>
  </section>

  <div class="edge-strip"></div>

  <section class="intro">
    <div class="kicker">NEW STRATEGIES FOR</div>
    <h1>DIABETIC RETINOPATHY</h1>
    <p>Diabetic Retinopathy (DR) is the leading cause of blindness among working-age Americans, according to the National Vision Research Council (NVRC). Yet, many cases could be prevented with regular eye exams and appropriate treatment. HealthPlan National has targeted diabetic eye disease management as a focus of care and has issued specific PQRI codes to report on eye disease management which can be reported by Primary Care doctors as well as Eye Care providers.</p>
    <div class="facts">
      <h2>DIABETIC RETINOPATHY FACTS</h2>
      <ul>
        <li>5 million Americans age 40 and older have DR</li>
        <li>16 million will have retinopathy by 2050</li>
        <li>50% of Diabetics acquire DR within 10 years of diagnosis</li>
        <li>94% of Diabetics acquire DR within 20 years of diagnosis</li>
        <li>Only 33% of diabetics have had an exam within 1 year</li>
        <li>Only 45% of diabetics have had an exam within 2 years</li>
        <li>Between 12,000 – 24,000 new cases of blindness from DR occur each year</li>
      </ul>
    </div>
  </section>

  <section class="clinical">
    <h2>THE CONDITION IS CHARACTERIZED BY <span class="accent">THESE SIGNS</span></h2>
    <ul class="signs">
      <li>Development of abnormal blood vessels (neovascularization) on or adjacent to the optic nerve and vitreous.</li>
      <li>Vitreous hemorrhage.</li>
      <li>Ischemia from decreased or blocked blood flow.</li>
    </ul>
    <h2>TREATMENT OF DIABETIC RETINOPATHY</h2>
    <p>Today, with the help of Primary Care Physicians and Endocrinologists, diabetics can maintain excellent vision through early detection and treatment. Early detection is critically important to avoid permanent damage to delicate retinal tissue. As the patient's diabetic doctor your recommendation to obtain annual eye exams is essential for proper patient compliance.</p>
    <h2>CURRENT TREATMENT STRATEGIES INCLUDE</h2>
    <div class="strategies">
      <ul>
        <li>Annual Dilated Eye Exams</li>
        <li>Annual Fundus Photography</li>
        <li>Ocular Coherence Tomography</li>
        <li>Fluorescein Angiography</li>
        <li>Intravitreal Anti-VEGF Injections</li>
      </ul>
      <ul>
        <li>Intravitreal Steroid Injections</li>
        <li>Laser Photocoagulation</li>
      </ul>
    </div>
  </section>

  <svg class="wave-bottom" viewBox="0 0 900 110" preserveAspectRatio="none" aria-hidden="true">
    <path d="M0,78 Q430,104 900,6 L900,110 L0,110 Z" fill="var(--blue)"/>
    <path d="M0,66 Q430,92 900,0 L900,6 Q430,104 0,78 Z" fill="#ffffff"/>
  </svg>
</main>
</body>
</html>
```